Webshop / TarnvikLoom

professional webshop page with possibility to buy and email etc. the logo is already part of the website. at the bottom of the file I would like to create a complete home page with all the details

Industry/Entity Type

It Professional

Number of Pages Required

1 page

Colors

Designer to choose colors to be used in the design.

```html
<!DOCTYPE html>
<html lang="en">
<head>
<meta charset="utf-8">
<title>TarnvikLoom – High quality CBD hemp</title>
<link href="https://fonts.googleapis.com/css2?family=Open+Sans:wght@400;600&family=Roboto+Condensed:wght@400&display=swap" rel="stylesheet">
<style>
:root{
  --green:#2f8a22;
  --green-dark:#1d6b17;
  --green-deep:#155512;
  --green-light:#4aa82d;
  --ink:#222;
  --text:#555;
  --white:#fff;
  --footer:#161616;
  --footer-line:#2d2d2d;
  --muted:#ccc;
}
*{margin:0;padding:0;box-sizing:border-box}
html,body{width:1200px;height:2609px;overflow:hidden}
body{position:relative;background:var(--white);font-family:"Open Sans",Arial,sans-serif;color:var(--ink)}
.abs{position:absolute}

/* header */
.site-header{position:absolute;left:0;top:0;width:1200px;height:104px;background:linear-gradient(180deg,var(--green) 0%,var(--green-dark) 100%);z-index:3}
.brand{position:absolute;display:flex;align-items:center;gap:8px;color:var(--white);font-weight:600;font-size:22px}
.brand-dot{width:14px;height:14px;border-radius:50%;background:var(--white)}
.site-header .brand{left:96px;top:36px}
.main-nav a{position:absolute;top:40px;color:var(--white);text-decoration:none;font-size:17px}
.login-btn{position:absolute;left:1036px;top:35px;width:72px;height:35px;border:1.5px solid var(--white);border-radius:18px;color:var(--white);font-size:15px;text-align:center;line-height:32px}

/* hero */
.hero{position:absolute;left:0;top:104px;width:1200px;height:526px;background:radial-gradient(ellipse at 70% 40%,#8a8c5e 0%,#6d5236 40%,#4a2d1a 100%)}
.hero-title{position:absolute;left:87px;top:196px;font-family:"Roboto Condensed",Arial,sans-serif;font-size:70px;color:var(--white);text-shadow:0 2px 6px rgba(0,0,0,.4);line-height:1}
.hero-sub{position:absolute;left:92px;top:272px;font-family:"Roboto Condensed",Arial,sans-serif;font-size:38px;color:#f2f2f2;text-shadow:0 2px 4px rgba(0,0,0,.4);line-height:1}
.slider-dots{position:absolute;left:1150px;top:196px}
.slider-dots span{display:block;width:7px;height:7px;border-radius:50%;background:#ddd;margin-bottom:12px}
.slider-dots span:first-child{background:var(--green-light)}
.hero-wave{position:absolute;left:0;top:580px}

/* about */
.section-title{position:absolute;font-weight:400;color:var(--ink);line-height:1}
.about-title{left:150px;top:775px;font-size:33px}
.about-text{position:absolute;left:146px;top:824px;width:480px;font-size:14.5px;line-height:24.5px;color:var(--text);text-align:justify}
.btn-green{position:absolute;background:var(--green);color:var(--white);font-size:12.5px;border-radius:18px;text-align:center}
.about-btn{left:146px;top:960px;width:117px;height:35px;line-height:35px}
.about-media{position:absolute;left:666px;top:744px;width:390px;height:265px;background:linear-gradient(135deg,#2b8a23,#1a6a15);box-shadow:0 6px 18px rgba(0,0,0,.25)}
.about-media-frame{position:absolute;left:10px;top:10px;right:10px;bottom:10px;border:1px solid rgba(255,255,255,.6)}
.about-media-item{position:absolute;left:32px;top:50px;width:326px;height:130px;border-radius:24px;background:linear-gradient(160deg,#e9eee9,#bfc8bf)}

/* products */
.products-band{position:absolute;left:0;top:1090px}
.products-title{left:0;width:1200px;text-align:center;top:1228px;font-size:38px;color:var(--white)}
.product-card{position:absolute;top:1315px;width:230px;height:219px;background:var(--white);box-shadow:0 3px 10px rgba(0,0,0,.25)}
.product-card svg{position:absolute;left:0;top:0}
.product-name{position:absolute;left:0;width:100%;top:182px;text-align:center;font-size:17px;color:var(--ink)}

/* articles */
.articles-title{left:0;width:1200px;text-align:center;top:1765px;font-size:33px}
.article{position:absolute;top:1836px;width:311px}
.article-img{width:311px;height:173px}
.article-meta{display:flex;margin-top:13px;height:22px;font-size:12.5px;line-height:22px;color:var(--white)}
.article-date{background:var(--green);width:72px;text-align:center}
.article-comments{background:#333;width:34px;display:flex;align-items:center;justify-content:center;gap:3px}
.article-title{margin-top:13px;font-size:16.5px;color:var(--ink);font-weight:400}
.article-text{margin-top:6px;font-size:12.5px;line-height:17px;color:var(--text)}
.article-more{margin-top:6px;font-size:13px;color:var(--green)}

/* footer */
.footer-wave{position:absolute;left:0;top:2250px}
.site-footer{position:absolute;left:0;top:2300px;width:1200px;height:309px;background:var(--footer)}
.site-footer .brand{left:122px;top:88px;font-size:22px}
.social{position:absolute;left:127px;top:168px;display:flex;gap:12px}
.social span{width:22px;height:22px;border-radius:3px;background:var(--white)}
.footer-head{position:absolute;top:58px;font-size:15px;color:var(--white)}
.quick-links{position:absolute;left:374px;top:98px;list-style:none}
.quick-links li{font-size:12.5px;color:var(--white);height:23px}
.quick-links li::before{content:"» ";}
.contact-row{position:absolute;left:577px;display:flex;gap:14px;font-size:12.5px;line-height:19px;color:var(--white)}
.contact-row svg{flex:none;margin-top:2px}
.mail-note{position:absolute;left:899px;top:95px;width:210px;font-size:12px;line-height:17px;color:var(--white)}
.mail-input{position:absolute;left:899px;top:135px;width:144px;height:29px;background:var(--white);font-size:12px;color:#999;padding:6px 8px}
.mail-submit{position:absolute;left:1043px;top:135px;width:58px;height:29px;background:var(--green);color:var(--white);font-size:12px;text-align:center;line-height:29px}
.footer-rule{position:absolute;left:88px;top:230px;width:1024px;height:1px;background:var(--footer-line)}
.copyright{position:absolute;left:0;width:1200px;text-align:center;top:262px;font-size:12.5px;color:var(--white)}
</style>
</head>
<body>

<header class="site-header">
  <div class="brand"><span class="brand-dot"></span>TarnvikLoom</div>
  <nav class="main-nav">
    <a style="left:482px">Home</a>
    <a style="left:582px">About us</a>
    <a style="left:703px">Products</a>
    <a style="left:824px">Blog</a>
    <a style="left:909px">Contacts</a>
  </nav>
  <div class="login-btn">Login</div>
</header>

<section class="hero" role="img" aria-label="Dried hemp flower buds spilling from a burlap sack beside a small oil bottle on a wooden table"></section>
<h1 class="hero-title">TarnvikLoom</h1>
<p class="hero-sub">High quality CBD hemp</p>
<div class="slider-dots"><span></span><span></span><span></span><span></span></div>
<svg class="hero-wave" width="1200" height="60" viewBox="0 0 1200 60">
  <path d="M0 18 C250 60 450 40 650 30 C850 20 1050 10 1200 20 L1200 60 L0 60Z" fill="var(--white)"/>
  <path d="M0 18 C250 60 450 40 650 30 C850 20 1050 10 1200 20 L1200 22 C1050 14 850 26 650 36 C450 46 250 60 0 26Z" fill="var(--green)"/>
</svg>

<h2 class="section-title about-title">About Us</h2>
<p class="about-text">It is a long established fact that a reader will be distracted by the readable content of a page when looking at its layout. The point of using Lorem Ipsum is that it has a more-or-less normal distribution of letters, as opposed to using 'Content here, content here', making it look like readable English. Many desktop publishing packages.</p>
<div class="btn-green about-btn">READ MORE »</div>
<div class="about-media">
  <div class="about-media-frame"></div>
  <div class="about-media-item" role="img" aria-label="Product tin of hemp goods"></div>
</div>

<svg class="products-band" width="1200" height="590" viewBox="0 0 1200 590">
  <defs>
    <linearGradient id="bandGrad" x1="0" y1="0" x2="0" y2="1">
      <stop offset="0" stop-color="#3f8f2b"/>
      <stop offset="0.5" stop-color="#2d7a22"/>
      <stop offset="1" stop-color="#3c8e2a"/>
    </linearGradient>
  </defs>
  <path d="M0 40 C250 0 500 40 700 35 C900 30 1050 0 1200 15 L1200 570 C1000 500 700 550 450 560 C250 568 100 540 0 560Z" fill="url(#bandGrad)" role="img" aria-label="Softly blurred hemp leaves and oil bottle background"/>
</svg>
<h2 class="section-title products-title">Our Products</h2>

<div class="product-card" style="left:110px">
  <svg width="230" height="170"><defs><linearGradient id="p1" x1="0" y1="0" x2="0" y2="1"><stop offset="0" stop-color="#2a2a2a"/><stop offset="1" stop-color="#9aa2a8"/></linearGradient></defs><path d="M0 0H230V150C150 120 80 125 0 150Z" fill="url(#p1)" role="img" aria-label="Oil vial among clear crystals"/></svg>
  <div class="product-name">Neque porro</div>
</div>
<div class="product-card" style="left:358px">
  <svg width="230" height="170"><defs><linearGradient id="p2" x1="0" y1="0" x2="0" y2="1"><stop offset="0" stop-color="#6b4a1e"/><stop offset="1" stop-color="#c8902f"/></linearGradient></defs><path d="M0 0H230V150C150 120 80 125 0 150Z" fill="url(#p2)" role="img" aria-label="Amber extract on a spoon"/></svg>
  <div class="product-name">Dolorem ipsum</div>
</div>
<div class="product-card" style="left:607px">
  <svg width="230" height="170"><defs><linearGradient id="p3" x1="0" y1="0" x2="0" y2="1"><stop offset="0" stop-color="#8a6a3a"/><stop offset="1" stop-color="#7a2e18"/></linearGradient></defs><path d="M0 0H230V150C150 120 80 125 0 150Z" fill="url(#p3)" role="img" aria-label="Tincture bottles with fresh herbs"/></svg>
  <div class="product-name">Porro Quisquam</div>
</div>
<div class="product-card" style="left:857px">
  <svg width="230" height="170"><defs><linearGradient id="p4" x1="0" y1="0" x2="0" y2="1"><stop offset="0" stop-color="#3a4a6a"/><stop offset="1" stop-color="#d19a2a"/></linearGradient></defs><path d="M0 0H230V150C150 120 80 125 0 150Z" fill="url(#p4)" role="img" aria-label="Golden shatter concentrate"/></svg>
  <div class="product-name">Ipsum Quia</div>
</div>

<h2 class="section-title articles-title">Latest Articles</h2>

<article class="article" style="left:94px">
  <div class="article-img" role="img" aria-label="Concentrate pieces with smoke" style="background:linear-gradient(160deg,#1d2f55,#b8892c)"></div>
  <div class="article-meta"><span class="article-date">Dec 03</span><span class="article-comments">&#9998;0</span></div>
  <h3 class="article-title">Neque porro quisquam dolorem</h3>
  <p class="article-text">It has survived not only five centuries, but also the leap into electronic typesetting,</p>
  <p class="article-more">Read More »</p>
</article>
<article class="article" style="left:442px">
  <div class="article-img" role="img" aria-label="Hemp leaf resting on a pile of seeds" style="background:linear-gradient(160deg,#5a7a2a,#4a2e1c)"></div>
  <div class="article-meta"><span class="article-date">Dec 03</span><span class="article-comments">&#9998;0</span></div>
  <h3 class="article-title">Porro quisquam est qui</h3>
  <p class="article-text">It has survived not only five centuries, but also the leap into electronic typesetting,</p>
  <p class="article-more">Read More »</p>
</article>
<article class="article" style="left:795px">
  <div class="article-img" role="img" aria-label="Rows of hemp plants in a greenhouse" style="background:linear-gradient(180deg,#c9d6c4,#4f8a2e 40%,#2f5e1c)"></div>
  <div class="article-meta"><span class="article-date">Dec 03</span><span class="article-comments">&#9998;0</span></div>
  <h3 class="article-title">Dolorem ipsum quia dolor</h3>
  <p class="article-text">It has survived not only five centuries, but also the leap into electronic typesetting,</p>
  <p class="article-more">Read More »</p>
</article>

<svg class="footer-wave" width="1200" height="60" viewBox="0 0 1200 60">
  <path d="M0 28 C200 18 400 20 560 40 C700 58 850 10 1200 8 L1200 60 L0 60Z" fill="var(--green-dark)"/>
  <path d="M0 34 C250 28 450 40 600 44 C800 50 1000 36 1200 44 L1200 60 L0 60Z" fill="var(--footer)"/>
</svg>

<footer class="site-footer">
  <div class="brand"><span class="brand-dot"></span>TarnvikLoom</div>
  <div class="social"><span></span><span></span><span></span><span></span></div>

  <div class="footer-head" style="left:369px">Quick links</div>
  <ul class="quick-links">
    <li>Testimonials</li>
    <li>Products</li>
    <li>Contact</li>
    <li>About us</li>
  </ul>

  <div class="footer-head" style="left:581px">Contacts</div>
  <div class="contact-row" style="top:94px">
    <svg width="13" height="17" viewBox="0 0 12 16"><path d="M6 0C2.7 0 0 2.6 0 5.8 0 10 6 16 6 16s6-6 6-10.2C12 2.6 9.3 0 6 0zm0 8.2A2.4 2.4 0 1 1 6 3.4a2.4 2.4 0 0 1 0 4.8z" fill="var(--white)"/></svg>
    <span>P.O Box 2287 Elmvale Ridge<br>QLD, 4190</span>
  </div>
  <div class="contact-row" style="top:145px">
    <svg width="13" height="13" viewBox="0 0 16 16"><path d="M3.6 0.5l2.4 2.8-1.4 2.2c1 2 3 4 5 5l2.2-1.4 2.8 2.4-1.3 3C7 15 1 9 .6 1.8z" fill="var(--white)"/></svg>
    <span>(61) 0400 118 275</span>
  </div>
  <div class="contact-row" style="top:172px">
    <svg width="14" height="11" viewBox="0 0 14 11"><rect width="14" height="11" fill="var(--white)"/><path d="M0 0l7 6 7-6" fill="none" stroke="var(--footer)" stroke-width="1.4"/></svg>
    <span>hello@tarnvikloom.shop</span>
  </div>

  <div class="footer-head" style="left:897px">Join our mailing list</div>
  <p class="mail-note">Your about us information would fit here nicely.</p>
  <div class="mail-input">Email address</div>
  <div class="mail-submit">Submit</div>

  <div class="footer-rule"></div>
  <p class="copyright">Copyright © 2017. All Rights Reserved</p>
</footer>

</body>
</html>
```